Property development & Investment company Need a logo & business card design

Our name is KT Estates Australia Pty Ltd
Need logo & business card design

Target Market(s)

People dealing in commercial property

Industry/Entity Type

Business

Contact Information for Business Card

KT Estates Australia
Peter Dunmore Mobile0419 703 646
Email Peter@quillbarrow.com.au

Font styles to use
Sans Serif

Requirements
Must have
• company name
• contact details
Nice to have
• KT Estates Bold
• Australia Not Bold
Should not have
• To busy of a look

```html
<!DOCTYPE html>
<html lang="en">
<head>
<meta charset="utf-8">
<title>KT Estates Australia – Business Card</title>
<link rel="stylesheet" href="https://fonts.googleapis.com/css2?family=Source+Sans+3:wght@400;600&display=swap">
<style>
  :root {
    --page-bg: #e4e7e8;
    --card-white: #ffffff;
    --card-dark: #232424;
    --lime: #8dc63f;
    --lime-light: #a9d66a;
    --slate: #6d6e70;
    --ink: #4a4b4d;
  }
  * { box-sizing: border-box; margin: 0; padding: 0; }
  html, body { width: 1200px; height: 960px; overflow: hidden; }
  body {
    background: var(--page-bg);
    font-family: "Source Sans 3", sans-serif;
    display: flex;
    flex-direction: column;
    align-items: center;
    justify-content: space-evenly;
  }
  .card {
    position: relative;
    width: 680px;
    height: 416px;
    overflow: hidden;
    box-shadow: 0 6px 20px rgba(0,0,0,0.15);
  }

  /* Front */
  .card-front { background: var(--card-white); }
  .identity {
    position: absolute;
    left: 50px;
    top: 56px;
    padding-left: 16px;
    border-left: 8px solid var(--lime);
  }
  .identity .person-name {
    font-size: 38px;
    font-weight: 400;
    color: var(--ink);
    line-height: 1.05;
  }
  .identity .job-title {
    font-size: 24px;
    font-weight: 400;
    color: var(--lime);
    line-height: 1.2;
  }
  .contact-list {
    position: absolute;
    left: 50px;
    top: 180px;
    list-style: none;
  }
  .contact-list li {
    display: flex;
    align-items: center;
    gap: 16px;
    font-size: 22px;
    color: var(--ink);
    margin-bottom: 14px;
  }
  .contact-list svg { width: 20px; height: 22px; flex: none; }
  .brand-mark {
    position: absolute;
    right: 64px;
    bottom: 110px;
    display: flex;
    align-items: center;
    gap: 10px;
    font-size: 28px;
    font-weight: 600;
    color: var(--lime);
  }
  .brand-mark .brand-square {
    width: 14px;
    height: 14px;
    background: var(--slate);
  }
  .band-row {
    position: absolute;
    left: 0;
    right: 0;
    bottom: 40px;
    height: 34px;
  }
  .band-row span { position: absolute; top: 0; bottom: 0; }
  .band-row .band-light { left: 0; width: 346px; background: var(--lime-light); }
  .band-row .band-grey { left: 354px; width: 194px; background: var(--slate); }
  .band-row .band-green { left: 556px; right: 0; background: var(--lime); }
  .band-base {
    position: absolute;
    left: 0;
    right: 0;
    bottom: 0;
    height: 40px;
    background: var(--lime);
  }

  /* Back */
  .card-back {
    background: linear-gradient(100deg, #1f2020 0%, #2c2d2d 55%, #222323 100%);
    display: flex;
    align-items: center;
    justify-content: center;
  }
  .back-brand {
    display: flex;
    align-items: center;
    gap: 16px;
    font-size: 46px;
    font-weight: 600;
    color: var(--lime);
  }
  .back-brand .brand-square {
    width: 22px;
    height: 22px;
    background: #ffffff;
  }
</style>
</head>
<body>

  <section class="card card-front" aria-label="Business card front">
    <div class="identity">
      <h1 class="person-name">Peter Dunmore</h1>
      <p class="job-title">Job Title</p>
    </div>
    <ul class="contact-list">
      <li>
        <svg viewBox="0 0 20 22" aria-hidden="true">
          <rect x="4" y="1" width="12" height="20" rx="2" fill="none" stroke="#8dc63f" stroke-width="2"/>
          <rect x="8" y="17" width="4" height="2" fill="#8dc63f"/>
        </svg>
        <span>0438 512 907</span>
      </li>
      <li>
        <svg viewBox="0 0 20 22" aria-hidden="true">
          <rect x="1" y="5" width="18" height="12" fill="#8dc63f"/>
          <path d="M1 5 L10 12 L19 5" fill="none" stroke="#ffffff" stroke-width="1.5"/>
        </svg>
        <span>Peter@quillbarrow.com.au</span>
      </li>
    </ul>
    <div class="brand-mark">
      <span class="brand-square" aria-hidden="true"></span>
      <span>KT Estates Australia</span>
    </div>
    <div class="band-row" aria-hidden="true">
      <span class="band-light"></span>
      <span class="band-grey"></span>
      <span class="band-green"></span>
    </div>
    <div class="band-base" aria-hidden="true"></div>
  </section>

  <section class="card card-back" aria-label="Business card back">
    <div class="back-brand">
      <span class="brand-square" aria-hidden="true"></span>
      <span>KT Estates Australia</span>
    </div>
  </section>

</body>
</html>
```